Inspiring Poster for Company Staff Room

What we need:
We want an awesome design to create a poster that will be plaque mounted in our staff room. We just went through a very motivating workshop to discover our "WHY" as a company...basically, to define the reason we are in business, and to define what motivates us to come to work every day. The poster must be motivating but really resonate with our team…we are not looking for a “typical” motivational poster that we can purchase off Brindleway!

Who we are:
We are a property management company, a team of 20 that is passionate about our investors, and residents who rent from us, but more importantly, we love helping people and making a difference in our industry. We are proud and work hard for every single 5 star Quorvix review we achieve.

Information for you:
We have included a mock up of the poster, which words we want, and the placement of them (in a general sense) but we need a designer to really bring this together in an inspiring poster that represents our company’s culture, feel, and fit. We have also included a logo file, as well as examples of our business cards, letterhead and thank you card already designed.
Here are the parameters:

(1) Poster size: 24” x 36”
(2) Full colour
(3) Must incorporate our company logo
(4) Must incorporate the following words:

Why do I come to work?

“To feel fulfilled by empathizing, educating and empowering our clients and co-workers so that we can build strong, impactful relationships”

Own the outcome

(5) Please see our website at www.larkmoorpm.example to get a feel for our company culture and for a better idea of our current company graphics

Target Market(s)

Our staff. Will not be seen by our clients

Industry/Entity Type

Real Estate

Font styles to use
Serif
Sans Serif

Requirements
Should not have
• Would not want this to be too "busy." if you can picture it, the poster will be mounted on the wall as soon as someone enters the room. The idea is to remind them each day why they come to work.

```html
<!DOCTYPE html>
<html lang="en">
<head>
<meta charset="utf-8">
<title>Why Do I Come to Work – Staff Room Poster</title>
<link rel="stylesheet" href="https://fonts.googleapis.com/css2?family=Archivo:ital,wght@0,700;1,400;1,900&family=Merriweather:wght@700&family=Libre+Baskerville&display=swap">
<style>
  :root {
    --sky: #4ec8f8;
    --sky-line: #8fd8f4;
    --azure: #3aaef0;
    --royal: #1652fc;
    --orange: #fa700f;
    --slate: #5b6966;
    --charcoal: #2d3536;
    --ink: #111111;
    --paper: #ffffff;
  }
  html, body {
    margin: 0;
    padding: 0;
    width: 911px;
    height: 1200px;
    overflow: hidden;
    background: var(--paper);
  }
  .poster {
    position: relative;
    width: 911px;
    height: 1200px;
    overflow: hidden;
  }
  .poster-shapes {
    position: absolute;
    inset: 0;
    display: block;
  }
  .brand {
    position: absolute;
    left: 282px;
    top: 68px;
    display: flex;
    align-items: center;
    gap: 12px;
    font-family: "Archivo", Arial, sans-serif;
    font-weight: 700;
    color: var(--azure);
  }
  .brand-square {
    width: 50px;
    height: 50px;
    background: var(--charcoal);
  }
  .brand-name {
    display: flex;
    flex-direction: column;
    line-height: 1;
  }
  .brand-name .primary {
    font-size: 36px;
    letter-spacing: 3px;
    text-transform: uppercase;
  }
  .brand-name .secondary {
    font-size: 13.5px;
    letter-spacing: 3.2px;
    text-transform: uppercase;
    margin-top: 6px;
  }
  .headline {
    position: absolute;
    left: 193px;
    top: 318px;
    margin: 0;
    font-family: "Merriweather", Georgia, serif;
    font-weight: 700;
    font-size: 36px;
    color: var(--azure);
    white-space: nowrap;
  }
  .purpose {
    position: absolute;
    left: 296px;
    top: 452px;
    width: 436px;
    margin: 0;
    font-family: "Libre Baskerville", Georgia, serif;
    font-size: 22px;
    line-height: 36px;
    letter-spacing: 1.4px;
    text-align: justify;
    color: var(--ink);
  }
  .motto {
    position: absolute;
    left: 196px;
    top: 752px;
    margin: 0;
    font-family: "Archivo", Arial, sans-serif;
    font-style: italic;
    font-size: 52px;
    line-height: 48px;
    color: var(--ink);
    letter-spacing: -1px;
  }
  .motto .strong { font-weight: 900; }
  .motto .light { font-weight: 400; }
</style>
</head>
<body>
<main class="poster">
  <svg class="poster-shapes" viewBox="0 0 1650 2200" width="911" height="1200" preserveAspectRatio="none" aria-hidden="true">
    <!-- header band -->
    <polyline points="147,280 147,53 1520,53 1520,280" fill="none" stroke="var(--sky-line)" stroke-width="5"/>
    <rect x="147" y="280" width="1375" height="98" fill="var(--orange)"/>
    <polygon points="520,277 838,452 1155,277" fill="var(--paper)" stroke="var(--sky)" stroke-width="5"/>
    <polygon points="153,90 420,215 420,397 153,275" fill="var(--royal)"/>
    <polygon points="1253,215 1520,90 1520,278 1253,397" fill="var(--slate)"/>

    <!-- content frames -->
    <polyline points="850,1697 222,1697 222,530 1362,530 1362,1188" fill="none" stroke="var(--sky-line)" stroke-width="4"/>
    <polyline points="850,1643 309,1643 309,475 1450,475 1450,1188" fill="none" stroke="var(--royal)" stroke-width="14"/>

    <!-- accent triangles and slants -->
    <polygon points="1155,628 1362,530 1362,725" fill="var(--royal)"/>
    <polygon points="302,790 510,887 302,985" fill="var(--slate)"/>
    <polygon points="1360,980 1522,907 1522,1030 1360,1108" fill="var(--orange)"/>
    <polygon points="150,1203 318,1275 318,1378 150,1310" fill="var(--orange)"/>

    <!-- corner block -->
    <rect x="1030" y="1330" width="300" height="300" fill="var(--azure)"/>

    <!-- footer band -->
    <rect x="147" y="1785" width="1375" height="100" fill="var(--orange)"/>
    <rect x="150" y="1890" width="1370" height="215" fill="var(--sky)"/>
    <polygon points="520,1887 838,1715 1155,1887" fill="var(--sky)"/>
    <polygon points="530,1890 820,1760 820,1955 530,2090" fill="var(--paper)"/>
    <polygon points="852,1760 1143,1890 1143,2090 852,1955" fill="var(--charcoal)"/>
  </svg>

  <header class="brand">
    <span class="brand-square"></span>
    <span class="brand-name">
      <span class="primary">Larkmoor</span>
      <span class="secondary">Property Management</span>
    </span>
  </header>

  <h1 class="headline">Why do I come to work?</h1>

  <p class="purpose">“To feel fulfilled by empathizing, educating and empowering our clients and co-workers so that we can build strong, impactful relationships”</p>

  <h2 class="motto"><span class="strong">Own</span> <span class="light">the</span><br><span class="strong">Outcome</span></h2>
</main>
</body>
</html>
```